Gin Bottle label

Hi, I would like a design based on a traditional, Vintage, Victorian type label.
The product is 'Thistle & Marrowroot Gin'
It will be 50cl and 40% vol.
The Gin will be dark brown in colour and attached is the types of bottle and a few ideas of the styles I like.
Many Thanks

```html
<!DOCTYPE html>
<html lang="en">
<head>
<meta charset="utf-8">
<title>Thistle &amp; Marrowroot Gin – Bottle Label</title>
<link rel="stylesheet" href="https://fonts.googleapis.com/css2?family=Roboto+Slab:wght@700&family=Oswald:wght@500&display=swap">
<style>
  :root {
    --backdrop: #ececec;
    --label-tan: #e9c794;
    --stripe-tan: #c9a36c;
    --panel-tan: #efca95;
    --ornament-tan: #cfa86e;
    --forest: #4a6a3a;
    --forest-deep: #3d5b30;
    --ink-white: #ffffff;
  }
  html, body {
    margin: 0;
    padding: 0;
    width: 1200px;
    height: 1000px;
    overflow: hidden;
    background: var(--backdrop);
  }
  .label-canvas {
    display: block;
    width: 1200px;
    height: 1000px;
  }
  .label-fill { fill: var(--label-tan); }
  .label-stripes { fill: url(#stripe-lines); }
  .label-edge { fill: none; stroke: var(--forest); stroke-width: 22; }
  .label-inner-edge { fill: none; stroke: var(--forest); stroke-width: 3; }
  .name-panel { fill: var(--panel-tan); stroke: var(--forest); stroke-width: 11; }
  .ornament-area { fill: url(#ornament-glow); }
  .product-name {
    font-family: "Roboto Slab", Georgia, serif;
    font-weight: 700;
    font-size: 100px;
  }
  .product-name .shadow { fill: var(--forest-deep); }
  .product-name .face {
    fill: var(--ink-white);
    stroke: var(--forest);
    stroke-width: 5;
    paint-order: stroke;
  }
  .side-note {
    font-family: "Oswald", "Arial Narrow", sans-serif;
    font-weight: 500;
    font-size: 24px;
    letter-spacing: 1px;
    fill: var(--forest);
  }
  .seal-ring { fill: var(--panel-tan); }
  .gin-seal { fill: var(--forest); stroke: var(--label-tan); stroke-width: 3; }
  .gin-word {
    font-family: "Oswald", "Arial Narrow", sans-serif;
    font-weight: 500;
    font-size: 62px;
    fill: var(--ink-white);
  }
</style>
</head>
<body>
<svg class="label-canvas" viewBox="0 0 1200 1000" xmlns="http://www.w3.org/2000/svg">
  <defs>
    <pattern id="stripe-lines" width="20" height="10" patternUnits="userSpaceOnUse">
      <rect x="0" y="0" width="20" height="2.5" fill="#c9a36c"/>
    </pattern>
    <radialGradient id="ornament-glow">
      <stop offset="0" stop-color="#cfa86e" stop-opacity="0.95"/>
      <stop offset="0.7" stop-color="#d8b47c" stop-opacity="0.7"/>
      <stop offset="1" stop-color="#e9c794" stop-opacity="0"/>
    </radialGradient>
    <path id="label-outline" d="M 55 260 Q 55 200 115 200 L 235 200 Q 270 200 275 165 Q 285 105 345 105 L 600 105 Q 660 105 670 165 Q 675 200 710 200 L 830 200 Q 890 200 890 260 L 890 660 Q 890 720 830 720 L 700 720 Q 660 720 650 760 Q 635 820 570 820 L 375 820 Q 310 820 295 760 Q 285 720 245 720 L 115 720 Q 55 720 55 660 Z"/>
  </defs>

  <g class="gin-label" transform="translate(128,40)">
    <use class="label-fill" href="#label-outline"/>
    <use class="label-stripes" href="#label-outline"/>

    <ellipse class="ornament-area" cx="472" cy="205" rx="190" ry="95" role="img" aria-label="Victorian filigree crest with scrolling flourishes"/>
    <ellipse class="ornament-area" cx="175" cy="272" rx="115" ry="38" role="img" aria-label="Scrolling corner flourish"/>
    <ellipse class="ornament-area" cx="770" cy="272" rx="115" ry="38" role="img" aria-label="Scrolling corner flourish"/>
    <ellipse class="ornament-area" cx="230" cy="660" rx="150" ry="45" role="img" aria-label="Scrolling flourish beside the seal"/>
    <ellipse class="ornament-area" cx="715" cy="660" rx="150" ry="45" role="img" aria-label="Scrolling flourish beside the seal"/>

    <use class="label-edge" href="#label-outline"/>
    <use class="label-inner-edge" href="#label-outline" transform="translate(472,462) scale(0.955 0.94) translate(-472,-462)"/>

    <rect class="name-panel" x="120" y="300" width="705" height="315" rx="55"/>

    <text class="side-note" transform="translate(145,458) rotate(90)" text-anchor="middle">50CL</text>
    <text class="side-note" transform="translate(800,458) rotate(90)" text-anchor="middle">40% VOL.</text>

    <g class="product-name" text-anchor="middle">
      <text class="shadow" x="478" y="430">THISTLE</text>
      <text class="face" x="472" y="424">THISTLE</text>
      <text class="shadow" x="478" y="558" textLength="590" lengthAdjust="spacingAndGlyphs">&amp; MARROWROOT</text>
      <text class="face" x="472" y="552" textLength="590" lengthAdjust="spacingAndGlyphs">&amp; MARROWROOT</text>
    </g>

    <circle class="seal-ring" cx="472" cy="688" r="95"/>
    <circle class="ornament-area" cx="472" cy="688" r="95" role="img" aria-label="Ornamental scrollwork ring framing the seal"/>
    <circle class="gin-seal" cx="472" cy="688" r="70"/>
    <text class="gin-word" x="472" y="710" text-anchor="middle">GIN</text>
  </g>
</svg>
</body>
</html>
```